Refined Sweets Table & Vessel Rental Needs a logo & business card design

I need a logo design and a business card design for a new candy buffet company based in Melbourne called "Pearl Sweets Table & Vessel Rental"(but the & Jar Hire part to be in smaller font). We set up candy bars with a wide variety of custom themes or to the customer's preference, we also hire out the glass jars if the customer prefers to do it themselves. But i want the emphasis on the front of the business card to be about the Candy Buffet and the jar hire can be at the back of the card. I would like to see designs that use the tiffany blue, or black and gold. I would like to see elegance, class but quite simple.

Industry/Entity Type

Business

Font styles to use
Script

```html
<!DOCTYPE html>
<html lang="en">
<head>
<meta charset="utf-8">
<title>Pearl Sweets Table &amp; Vessel Rental – Business Card</title>
<link rel="stylesheet" href="https://fonts.googleapis.com/css2?family=Cormorant+Garamond:wght@500&family=Questrial&display=swap">
<style>
  :root {
    --page-bg: #ffffff;
    --gold-light: #f3e7b4;
    --gold-mid: #dcc57e;
    --gold-deep: #b8962f;
    --gold-text: #a8861f;
    --tiffany: #1bb89a;
    --tiffany-soft: #7fd8c2;
    --cream: #f6efd6;
    --white: #ffffff;
    --shadow: rgba(0, 0, 0, 0.18);
  }
  * { box-sizing: border-box; margin: 0; padding: 0; }
  html, body {
    width: 1200px;
    height: 900px;
    overflow: hidden;
    background: var(--page-bg);
  }
  .canvas {
    position: relative;
    width: 1200px;
    height: 900px;
  }
  .card {
    position: absolute;
    top: 305px;
    width: 530px;
    height: 295px;
    border-radius: 26px;
    overflow: hidden;
    box-shadow: 0 14px 30px var(--shadow);
  }
  .card--front { left: 55px; }
  .card--back  { left: 615px; background: var(--tiffany); }

  .card__art {
    position: absolute;
    inset: 0;
    width: 100%;
    height: 100%;
  }

  /* Front */
  .front-name {
    position: absolute;
    left: 40px;
    top: 108px;
    width: 250px;
    font-family: "Cormorant Garamond", serif;
    font-weight: 500;
    color: var(--gold-text);
    line-height: 1.05;
  }
  .front-name__main { display: block; font-size: 38px; }
  .front-name__sub  { display: block; font-size: 22px; margin-top: 6px; }

  /* Back */
  .back-content {
    position: absolute;
    inset: 0;
    text-align: center;
    color: var(--white);
  }
  .back-name {
    position: absolute;
    top: 40px;
    left: 0;
    right: 0;
    font-family: "Cormorant Garamond", serif;
    font-weight: 500;
    line-height: 1.05;
  }
  .back-name__main { display: block; font-size: 32px; }
  .back-name__sub  { display: block; font-size: 17px; margin-top: 4px; }
  .back-tagline {
    position: absolute;
    top: 145px;
    left: 0;
    right: 0;
    font-family: "Questrial", sans-serif;
    line-height: 1.2;
  }
  .back-tagline__lead { display: block; font-size: 22px; }
  .back-tagline__rest { display: block; font-size: 19px; }
  .back-contact {
    position: absolute;
    top: 215px;
    left: 0;
    right: 0;
    font-family: "Questrial", sans-serif;
    font-size: 15px;
  }
</style>
</head>
<body>
<main class="canvas">

  <section class="card card--front" aria-label="Business card front">
    <svg class="card__art" viewBox="0 0 530 295" preserveAspectRatio="none" aria-hidden="false">
      <defs>
        <linearGradient id="goldSheen" x1="0" y1="0" x2="1" y2="1">
          <stop offset="0" stop-color="#e9d795"/>
          <stop offset="0.45" stop-color="#f5eabb"/>
          <stop offset="1" stop-color="#d7bd6f"/>
        </linearGradient>
        <radialGradient id="jarTones" cx="0.55" cy="0.55" r="0.7">
          <stop offset="0" stop-color="#eee6c8"/>
          <stop offset="0.5" stop-color="#cfe3cf"/>
          <stop offset="1" stop-color="#d8c892"/>
        </radialGradient>
      </defs>
      <rect class="front-bg" width="530" height="295" fill="url(#goldSheen)"/>
      <path class="front-swoosh" d="M300 0 C250 80 255 210 330 295 L350 295 C285 210 278 90 330 0 Z" fill="var(--tiffany-soft)"/>
      <path class="front-photo" role="img" aria-label="Photo of a glass candy jar filled with sweets, tied with a mint satin ribbon"
            d="M318 0 C266 85 272 210 345 295 L530 295 L530 0 Z" fill="url(#jarTones)"/>
    </svg>
    <h1 class="front-name">
      <span class="front-name__main">Pearl Sweets Table</span>
      <span class="front-name__sub">&amp; Vessel Rental</span>
    </h1>
  </section>

  <section class="card card--back" aria-label="Business card back">
    <div class="back-content">
      <h2 class="back-name">
        <span class="back-name__main">Pearl Sweets Table</span>
        <span class="back-name__sub">&amp; Vessel Rental</span>
      </h2>
      <p class="back-tagline">
        <span class="back-tagline__lead">Enjoy in some sweet decadance</span>
        <span class="back-tagline__rest">at your next special event</span>
      </p>
      <p class="back-contact">Please Contact Clara on 0412 555 018</p>
    </div>
  </section>

</main>
</body>
</html>
```